Brightpath Dental Studio

Please go to www.brightpathdentalstudio.example and obtain the current company logo.
Doctors name are
Marita Velbonne, DDS
Denis Kalb, DMD
Addresses are
318 Larchmont Ave
Teaneck, NJ 07666
201-555-0147
And
872 14th St.
West New York, NJ 07093
201-555-0182
Theme of the business card should feel modrrn and similar to the website.
Front side should include company logo, doctors name, addresses, phone numbers.
Back of the card should include blank lines for patient's name. Date and time for next scheduled appointment. And notice of 24-hr cancellation courtesy policy.
Dental

```html
<!DOCTYPE html>
<html lang="en">
<head>
<meta charset="utf-8">
<title>Brightpath Dental Studio — Business Card</title>
<link rel="stylesheet" href="https://fonts.googleapis.com/css2?family=Montserrat:wght@400;600;700&family=Open+Sans:wght@400;600&display=swap">
<style>
  :root {
    --navy: #1c2f6b;
    --navy-deep: #142353;
    --white: #ffffff;
    --paper: #f4f5f7;
    --ink: #3d4250;
    --muted: #8a909e;
    --backdrop: #e6e3de;
  }
  * { box-sizing: border-box; margin: 0; padding: 0; }
  html, body { width: 773px; height: 1200px; overflow: hidden; }
  body {
    background: var(--backdrop);
    font-family: "Open Sans", Arial, sans-serif;
    color: var(--ink);
    position: relative;
  }
  .card {
    position: absolute;
    left: 56px;
    width: 660px;
    height: 378px;
    background: var(--white);
    border-radius: 10px;
    overflow: hidden;
    box-shadow: 0 6px 18px rgba(0,0,0,.18);
  }
  .card--front { top: 170px; }
  .card--back { top: 650px; }
  .card svg.shapes { position: absolute; inset: 0; }
  .brand {
    position: absolute;
    display: flex;
    align-items: center;
    gap: 10px;
  }
  .brand__dot {
    flex: none;
    width: 30px; height: 30px; border-radius: 50%;
    border: 3px solid var(--navy);
  }
  .brand__name {
    font-family: "Montserrat", Arial, sans-serif;
    font-weight: 700;
    font-size: 22px;
    color: var(--navy);
    line-height: 1.1;
    letter-spacing: .5px;
  }
  .brand--front { left: 40px; top: 62px; }
  .brand--back { left: 210px; top: 40px; }
  .website {
    position: absolute;
    font-size: 11px;
    color: var(--muted);
    letter-spacing: .3px;
  }
  .website--front { left: 40px; top: 130px; }
  .website--back { left: 250px; top: 84px; }
  .doctor { position: absolute; font-size: 11.5px; line-height: 1.65; }
  .doctor__name {
    font-family: "Montserrat", Arial, sans-serif;
    font-weight: 600;
    font-size: 17px;
    line-height: 1.2;
  }
  .doctor__title { font-size: 11px; margin-bottom: 10px; opacity: .8; }
  .doctor__line { display: flex; align-items: flex-start; gap: 8px; }
  .doctor__line svg { flex: none; margin-top: 3px; }
  .doctor--primary { left: 40px; top: 170px; color: var(--ink); }
  .doctor--secondary { left: 392px; top: 60px; color: var(--white); }
  .appointment {
    position: absolute;
    left: 300px; top: 120px; width: 320px;
    font-size: 12px; color: var(--ink);
  }
  .appointment__row { display: flex; align-items: flex-end; gap: 8px; margin-bottom: 22px; }
  .appointment__blank { flex: 1; border-bottom: 1px solid var(--muted); height: 14px; }
  .notice {
    position: absolute;
    left: 300px; top: 270px; width: 320px;
    font-size: 11px; color: var(--muted);
  }
</style>
</head>
<body>

<section class="card card--front" aria-label="Card front">
  <svg class="shapes" width="660" height="378" viewBox="0 0 660 378">
    <polygon points="360,0 600,0 640,378 400,378" fill="var(--navy)"/>
    <polygon points="590,0 604,0 644,378 630,378" fill="var(--navy-deep)"/>
  </svg>
  <div class="brand brand--front">
    <span class="brand__dot"></span>
    <span class="brand__name">Brightpath<br>Dental Studio</span>
  </div>
  <p class="website website--front">www.brightpathdentalstudio.example</p>

  <div class="doctor doctor--primary">
    <p class="doctor__name">Denis Kalb</p>
    <p class="doctor__title">DMD</p>
    <p class="doctor__line">
      <svg width="10" height="13" viewBox="0 0 10 13"><path d="M5 0a5 5 0 0 1 5 5c0 3.5-5 8-5 8S0 8.5 0 5a5 5 0 0 1 5-5z" fill="var(--navy)"/><circle cx="5" cy="5" r="1.8" fill="var(--white)"/></svg>
      <span>872 14th St.<br>West New York, NJ 07093</span>
    </p>
    <p class="doctor__line">
      <svg width="11" height="11" viewBox="0 0 24 24"><path d="M6.6 10.8a15 15 0 0 0 6.6 6.6l2.2-2.2a1 1 0 0 1 1-.25 11.4 11.4 0 0 0 3.6.6 1 1 0 0 1 1 1V20a1 1 0 0 1-1 1A17 17 0 0 1 3 4a1 1 0 0 1 1-1h3.5a1 1 0 0 1 1 1c0 1.25.2 2.45.6 3.6a1 1 0 0 1-.25 1z" fill="var(--navy)"/></svg>
      <span>201-555-0182</span>
    </p>
  </div>

  <div class="doctor doctor--secondary">
    <p class="doctor__name">Marita Velbonne</p>
    <p class="doctor__title">DDS</p>
    <p class="doctor__line">
      <svg width="10" height="13" viewBox="0 0 10 13"><path d="M5 0a5 5 0 0 1 5 5c0 3.5-5 8-5 8S0 8.5 0 5a5 5 0 0 1 5-5z" fill="var(--white)"/><circle cx="5" cy="5" r="1.8" fill="var(--navy)"/></svg>
      <span>318 Larchmont Ave<br>Teaneck, NJ 07666</span>
    </p>
    <p class="doctor__line">
      <svg width="11" height="11" viewBox="0 0 24 24"><path d="M6.6 10.8a15 15 0 0 0 6.6 6.6l2.2-2.2a1 1 0 0 1 1-.25 11.4 11.4 0 0 0 3.6.6 1 1 0 0 1 1 1V20a1 1 0 0 1-1 1A17 17 0 0 1 3 4a1 1 0 0 1 1-1h3.5a1 1 0 0 1 1 1c0 1.25.2 2.45.6 3.6a1 1 0 0 1-.25 1z" fill="var(--white)"/></svg>
      <span>201-555-0147</span>
    </p>
  </div>
</section>

<section class="card card--back" aria-label="Card back">
  <svg class="shapes" width="660" height="378" viewBox="0 0 660 378">
    <polygon points="0,0 150,0 100,378 0,378" fill="var(--navy)"/>
    <polygon points="150,0 164,0 114,378 100,378" fill="var(--navy-deep)"/>
    <polygon points="560,378 660,300 660,378" fill="var(--navy)"/>
  </svg>
  <div class="brand brand--back">
    <span class="brand__dot"></span>
    <span class="brand__name">Brightpath Dental Studio</span>
  </div>
  <p class="website website--back">www.brightpathdentalstudio.example</p>

  <div class="appointment">
    <div class="appointment__row"><span>Mr./Ms.</span><span class="appointment__blank"></span></div>
    <div class="appointment__row"><span>has an appointment on</span><span class="appointment__blank"></span></div>
    <div class="appointment__row">
      <span>Date</span><span class="appointment__blank"></span>
      <span>Time</span><span class="appointment__blank"></span>
    </div>
  </div>
  <p class="notice">If unable to keep appointment, please give 24 hour notice.</p>
</section>

</body>
</html>
```